Larchmere Valley College

We are looking to update our current webpage at www.larchmerevalley.ca. We would like to make it modern, fresh and appealing to students. We want to keep our logo the same with the logo colours blended in as the primary colours and focus. We are open to reconfiguring content as well.
Reason: Hi, In the next 3 days we will have narrowed our search to 3 designs and will make a choice before the final deadline...
Industry/Entity Type
College

```html
<!DOCTYPE html>
<html lang="en">
<head>
<meta charset="utf-8">
<title>Larchmere Valley College</title>
<link rel="stylesheet" href="https://fonts.googleapis.com/css2?family=Arvo:wght@700&family=Lato:wght@400;700&display=swap">
<style>
:root{
  --navy:#14204f;
  --navy-dark:#0c1538;
  --ink:#2b2b2b;
  --muted:#555a66;
  --light:#eceef2;
  --white:#ffffff;
  --black:#0e0e0e;
  --rule:#c9ccd4;
}
*{box-sizing:border-box;margin:0;padding:0}
html,body{width:1200px;height:2824px;overflow:hidden;background:var(--white)}
body{font-family:"Lato",sans-serif;color:var(--ink);position:relative}
.wrap{position:absolute;left:130px;width:940px}
.heading{font-family:"Arvo",serif;color:var(--navy);font-weight:700}
.btn{display:inline-block;background:var(--navy);color:var(--white);font-weight:700;font-size:16px;border-radius:6px;padding:0 26px;line-height:38px}

/* header */
.header{position:absolute;top:0;left:0;width:1200px;height:122px;background:var(--white)}
.utility{position:absolute;left:612px;top:0;width:447px;height:24px;background:var(--navy);border-radius:0 0 10px 10px;display:flex;justify-content:space-around;align-items:center;color:var(--white);font-size:12px;font-weight:700}
.brand{position:absolute;left:134px;top:18px;display:flex;align-items:center;gap:12px}
.brand-dot{width:40px;height:40px;border-radius:50%;background:var(--navy)}
.brand-name{font-family:"Arvo",serif;font-weight:700;color:var(--navy);font-size:22px;line-height:26px;width:200px}
.search{position:absolute;left:725px;top:59px;width:176px;height:28px;border:1px solid #b9bcc4;font-size:11px;color:#8a8d96;padding:0 8px;line-height:26px}
.search span.go{position:absolute;right:0;top:0;width:26px;height:26px;background:#c4c6cc}
.social{position:absolute;left:922px;top:56px;display:flex;gap:6px}
.social i{width:32px;height:32px;border-radius:50%;border:2px solid var(--navy);display:block}
.social i:last-child{border-color:#c0392b}

/* nav */
.nav{position:absolute;top:122px;left:130px;width:940px;height:47px;background:var(--navy-dark);display:flex;justify-content:space-between;align-items:center;padding-right:14px;z-index:2}
.nav a{color:var(--white);text-decoration:none;font-size:14px;padding:0 14px;line-height:47px}
.nav a.active{background:#050a22;font-weight:700}

/* hero */
.hero{position:absolute;top:122px;left:0;width:1200px;height:560px;background:linear-gradient(160deg,#3f5a36 0%,#6f8a5a 30%,#b49a86 55%,#5d6f86 80%,#2f3e5a 100%)}
.hero-caption{position:absolute;left:0;bottom:0;width:100%;height:89px;background:rgba(12,21,56,.75);text-align:center;color:var(--white);padding-top:14px}
.hero-caption h1{font-size:30px;font-weight:700;letter-spacing:.5px;text-transform:uppercase}
.hero-caption p{font-size:14px;margin-top:4px}

/* welcome */
.welcome{top:738px;text-align:center}
.welcome h2{font-size:28px}
.rule{width:300px;height:1px;background:var(--rule);margin:14px auto 16px}
.welcome p{font-size:14px;line-height:22px;color:var(--ink)}
.welcome .btn{margin-top:14px}

/* videos */
.videos{position:absolute;top:995px;left:0;width:1200px;height:283px;background:linear-gradient(90deg,#2a1f1a 0%,#3b4a3d 40%,#1e3a33 60%,#2a211c 100%)}
.videos::after{content:"";position:absolute;inset:0;background:rgba(10,14,28,.55)}
.videos .inner{position:absolute;left:130px;width:940px;top:34px;text-align:center;color:var(--white);z-index:1}
.videos h2{font-family:"Arvo",serif;font-size:28px;margin-bottom:18px}
.videos p{font-size:14px;line-height:22px}
.play{margin:24px auto 0;width:56px;height:56px}

/* campus */
.campus{top:1330px;text-align:center}
.campus h2{font-size:28px}
.campus .rule{width:330px;margin:12px auto 14px}
.cards{display:flex;justify-content:space-between}
.card{width:278px}
.photo{border:1px solid #d6d8de;padding:6px;height:186px;background:var(--white)}
.photo div{width:100%;height:100%}
.card h3{font-size:18px;color:var(--navy);margin:22px 0 8px;font-weight:700}
.card p{font-size:14px;line-height:22px;color:var(--muted)}
.card .btn{margin-top:14px}

/* admissions & news */
.lower{position:absolute;top:1805px;left:0;width:1200px;height:402px;background:linear-gradient(180deg,#e8e9ec,#dfe1e5)}
.admissions{position:absolute;left:134px;top:54px}
.admissions h2,.news h2{font-size:26px;margin-bottom:22px}
.admissions ul{list-style:none}
.admissions li{display:flex;align-items:center;gap:14px;font-size:14px;height:35px;color:var(--ink)}
.admissions svg{width:18px;height:18px}
.news{position:absolute;left:605px;top:54px;width:466px}
.news-items{display:flex;gap:60px;padding-left:2px}
.news-item{width:200px}
.news-thumb{border:1px solid #cfd2d8;padding:5px;background:var(--white);height:104px}
.news-thumb div{width:100%;height:100%}
.news-item h4{font-size:14px;font-weight:700;color:var(--navy);margin-top:14px}
.news-item p{font-size:14px;line-height:21px;color:var(--ink);font-weight:700}
.news-item a{font-size:14px;color:var(--navy);text-decoration:none}

/* contact */
.contact{position:absolute;top:2207px;left:0;width:1200px;height:581px;background:var(--navy);color:var(--white)}
.contact-head{position:absolute;left:0;width:100%;top:50px;text-align:center}
.envelope{width:66px;height:66px;margin:0 auto}
.contact-head h2{font-size:26px;font-weight:400;margin-top:8px}
.contact-head p{font-size:13px;line-height:18px;margin-top:8px;color:#d8dbe6}
.contact-rule{position:absolute;left:130px;top:218px;width:940px;height:1px;background:rgba(255,255,255,.35)}
.col h3{font-size:20px;font-weight:700;margin-bottom:16px}
.form{position:absolute;left:134px;top:238px;width:306px}
.field{background:var(--white);border-radius:5px;height:38px;margin-bottom:12px;color:#9a9da6;font-size:11px;padding:10px 12px}
.field.tall{height:80px}
.send{display:inline-block;background:var(--black);color:var(--white);font-weight:700;font-size:14px;width:140px;line-height:38px;text-align:center;border-radius:6px;margin-top:8px}
.map-col{position:absolute;left:495px;top:238px}
.map{width:320px;height:200px;border:6px solid var(--white);background:linear-gradient(135deg,#d9e5cf,#e9ece2 50%,#cfdcc4)}
.find{position:absolute;left:870px;top:238px;width:210px}
.find li{list-style:none;display:flex;gap:12px;font-size:13px;line-height:19px;margin-bottom:14px}
.find svg{flex:none;width:14px;height:16px;margin-top:2px}
.squares{display:flex;gap:14px;margin-top:6px}
.squares i{width:22px;height:22px;background:var(--white);display:block}

.footer{position:absolute;top:2788px;left:0;width:1200px;height:36px;background:var(--black);color:#cfd1d6;font-size:12px;text-align:center;line-height:36px}
</style>
</head>
<body>

<header class="header">
  <div class="utility"><span>Apply Today</span><span>Donate</span><span>Library</span><span>Text For Info</span></div>
  <div class="brand"><span class="brand-dot"></span><span class="brand-name">Larchmere Valley College</span></div>
  <div class="search">Search your Subject<span class="go"></span></div>
  <div class="social"><i></i><i></i><i></i><i></i></div>
</header>

<nav class="nav">
  <a class="active">Home</a><a>About Us</a><a>Consider Larchmere</a><a>Current students</a><a>Alumni</a><a>Supporters</a><a>News &amp; Event</a><a>Larchmere Park</a>
</nav>

<section class="hero" role="img" aria-label="Photo of four smiling students sitting outdoors with notebooks">
  <div class="hero-caption">
    <h1>We will help you to understand friendly education</h1>
    <p>Lorem ipsum dolor sit amet, consectetuer adipiscing elit, sed diam nonummy nibh euismod tincidunt ut laoreet dolore.</p>
  </div>
</section>

<section class="wrap welcome">
  <h2 class="heading">Welcome Larchmere Valley College</h2>
  <div class="rule"></div>
  <p>Lorem ipsum dolor sit amet, consectetur adipiscing elit. Aenean et dignissim sem, interdum risus. Vestibulum consectetur nisi mollis diam pulvinar adipiscing. Vestibulum ut urna nec nibh adipiscing facilisis. Etiam auctor porta lacus ac luctus. Praesent ac libero fermentum, rhoncus magna a, dapibus mauris. Nam ut auctor justo. Sed ante odio, luctus quis nequ nec, adipiscing eleifend arcu. Integer nunc turpis, porttitor at lorem ut. Etiam auctor porta lacus ac luctus. Praesent ac libero fermentum, rhoncus magna.</p>
  <span class="btn">Read More</span>
</section>

<section class="videos" role="img" aria-label="Photo of the college entrance sign in front of a brick building">
  <div class="inner">
    <h2>Larchmere Videos</h2>
    <p>Lorem ipsum dolor sit amet, consectetur adipiscing elit. Aenean et dignissim sem, interdum risus. Vestibulum consectetur nisi mollis diam pulvinar adipiscing. Vestibulum ut urna nec nibh adipiscing facilisis. Etiam auctor porta lacus ac luctus. Praesent ac libero fermentum, rhoncus. consectetur adipiscing elit. Aenean et dignissim sem, interdum risus. Vestibulum consectetur nisi mollis diam pulvinar adipiscing.</p>
    <svg class="play" viewBox="0 0 56 56"><circle cx="28" cy="28" r="25" fill="none" stroke="#fff" stroke-width="3"/><path d="M23 18 L38 28 L23 38 Z" fill="#fff"/></svg>
  </div>
</section>

<section class="wrap campus">
  <h2 class="heading">Our Campus</h2>
  <div class="rule"></div>
  <div class="cards">
    <div class="card">
      <div class="photo"><div role="img" aria-label="Aerial campus map with location pins" style="background:linear-gradient(135deg,#3b4a7a,#5b6a8e 50%,#3e5a4a)"></div></div>
      <h3>Campur Map</h3>
      <p>Lorem ipsum dolor sit amet, consectetur adipiscing elit. Aenean et dignissim sem, interdum risus. Vestibulum consectetu</p>
      <span class="btn">Read More</span>
    </div>
    <div class="card">
      <div class="photo"><div role="img" aria-label="Street map showing directions to the college" style="background:linear-gradient(135deg,#dfe6d3,#eceee6 50%,#d5e0c8)"></div></div>
      <h3>Map &amp; Directions</h3>
      <p>Lorem ipsum dolor sit amet, consectetur adipiscing elit. Aenean et dignissim sem, interdum risus. Vestibulum consectetu</p>
      <span class="btn">Read More</span>
    </div>
    <div class="card">
      <div class="photo"><div role="img" aria-label="Photo of the college chapel hall with rows of chairs" style="background:linear-gradient(180deg,#d9d6d0,#b8a898 60%,#8a6e5a)"></div></div>
      <h3>Photo Tour</h3>
      <p>Lorem ipsum dolor sit amet, consectetur adipiscing elit. Aenean et dignissim sem, interdum risus. Vestibulum consectetu</p>
      <span class="btn">Read More</span>
    </div>
  </div>
</section>

<section class="lower" role="img" aria-label="Faint photo of a lecture hall as background">
  <div class="admissions">
    <h2 class="heading">Our Admissions</h2>
    <ul>
      <li><svg viewBox="0 0 18 18"><circle cx="9" cy="9" r="9" fill="#14204f"/><path d="M5 9.5l2.6 2.6L13 6.5" fill="none" stroke="#fff" stroke-width="2"/></svg>Download The Full Catalogue</li>
      <li><svg viewBox="0 0 18 18"><circle cx="9" cy="9" r="9" fill="#14204f"/><path d="M5 9.5l2.6 2.6L13 6.5" fill="none" stroke="#fff" stroke-width="2"/></svg>Apply Today (Application Package)</li>
      <li><svg viewBox="0 0 18 18"><circle cx="9" cy="9" r="9" fill="#14204f"/><path d="M5 9.5l2.6 2.6L13 6.5" fill="none" stroke="#fff" stroke-width="2"/></svg>Information Request</li>
      <li><svg viewBox="0 0 18 18"><circle cx="9" cy="9" r="9" fill="#14204f"/><path d="M5 9.5l2.6 2.6L13 6.5" fill="none" stroke="#fff" stroke-width="2"/></svg>Browse our Programs</li>
      <li><svg viewBox="0 0 18 18"><circle cx="9" cy="9" r="9" fill="#14204f"/><path d="M5 9.5l2.6 2.6L13 6.5" fill="none" stroke="#fff" stroke-width="2"/></svg>Download Forms</li>
      <li><svg viewBox="0 0 18 18"><circle cx="9" cy="9" r="9" fill="#14204f"/><path d="M5 9.5l2.6 2.6L13 6.5" fill="none" stroke="#fff" stroke-width="2"/></svg>Admissions Information</li>
      <li><svg viewBox="0 0 18 18"><circle cx="9" cy="9" r="9" fill="#14204f"/><path d="M5 9.5l2.6 2.6L13 6.5" fill="none" stroke="#fff" stroke-width="2"/></svg>Campus Directory</li>
    </ul>
  </div>
  <div class="news">
    <h2 class="heading">News &amp; Event</h2>
    <div class="news-items">
      <div class="news-item">
        <div class="news-thumb"><div role="img" aria-label="Photo of a business meeting" style="background:linear-gradient(90deg,#e6e9ee,#9aa6b8 50%,#e3e6ea)"></div></div>
        <h4>November 22, 2014</h4>
        <p>Lorem ipsum dolor sit amet consectetur adipiscing elit.</p>
        <a>Read More »</a>
      </div>
      <div class="news-item">
        <div class="news-thumb"><div role="img" aria-label="Photo of two people in discussion" style="background:linear-gradient(90deg,#dfe3e8,#7c6f86 50%,#d7dbe1)"></div></div>
        <h4>November 22, 2014</h4>
        <p>Lorem ipsum dolor sit amet consectetur adipiscing elit.</p>
        <a>Read More »</a>
      </div>
    </div>
  </div>
</section>

<section class="contact">
  <div class="contact-head">
    <svg class="envelope" viewBox="0 0 66 66"><circle cx="33" cy="33" r="31" fill="none" stroke="#fff" stroke-width="3"/><rect x="20" y="24" width="26" height="18" fill="#fff"/><path d="M20 24l13 10 13-10" fill="none" stroke="#14204f" stroke-width="2"/></svg>
    <h2>Contact Us</h2>
    <p>Please, Feel free to contact anytime. it's always<br>a pleasure meeting new student.</p>
  </div>
  <div class="contact-rule"></div>

  <div class="col form">
    <h3>Drop Your Question</h3>
    <div class="field">Name</div>
    <div class="field">Email</div>
    <div class="field tall">Message</div>
    <span class="send">SEND</span>
  </div>

  <div class="col map-col">
    <h3>Location Map</h3>
    <div class="map" role="img" aria-label="Street map with a pin marking the college"></div>
  </div>

  <div class="col find">
    <h3>Find Us</h3>
    <ul>
      <li><svg viewBox="0 0 14 16"><path d="M7 0a5 5 0 0 0-5 5c0 4 5 11 5 11s5-7 5-11a5 5 0 0 0-5-5z" fill="#fff"/><circle cx="7" cy="5" r="2" fill="#14204f"/></svg><span>123 euismod cidun ut laoreet laoreet dol magna aliquam PG Fesgalt</span></li>
      <li><svg viewBox="0 0 14 16"><path d="M3 1h3l1 4-2 1c1 2 2 3 4 4l1-2 4 1v3c0 1-1 2-2 2C6 14 0 8 1 3c0-1 1-2 2-2z" fill="#fff"/></svg><span>(123) 456 - 7890</span></li>
      <li><svg viewBox="0 0 14 16"><rect x="3" y="1" width="8" height="14" rx="1.5" fill="#fff"/><rect x="4.5" y="3" width="5" height="8" fill="#14204f"/></svg><span>(123) 456 - 7890</span></li>
      <li><svg viewBox="0 0 14 16"><rect x="0" y="3" width="14" height="10" fill="#fff"/><path d="M0 3l7 5 7-5" fill="none" stroke="#14204f" stroke-width="1.5"/></svg><span>info@larchmerevalley.ca</span></li>
    </ul>
    <div class="squares"><i></i><i></i><i></i><i></i></div>
  </div>
</section>

<footer class="footer">Copyright © 2014 Larchmerevalley. All Right Reserved</footer>

</body>
</html>
```